Business Card Design Project

I require a business card design that looks professional for a small building company. Holloway Builders is the name of the company and i don't want to use a house or building design for a logo. I require a logo design for the card incorporating the name Holloway Builders but designed smartly.

We are a Registered Building Practitioner so the small logo attached must also be used on the card.

We cover a large range of Building / Construction, Concrete, Steelwork. Not sure how to implement this.

Colors are flexible, maybe a dark grey background with white writting over it, but i am keen to see other options.

Thanks.

Target Market(s)

Anyone

Industry/Entity Type

Building

Requirements
Must have
• The logo attached must be incorporated - can be small
A logo for my company needs to be included - using Holloway Builders as the base with no picture of a house or buildings.

```html
<!DOCTYPE html>
<html lang="en">
<head>
<meta charset="utf-8">
<title>Holloway Builders – Business Card Options</title>
<link rel="stylesheet" href="https://fonts.googleapis.com/css2?family=Oswald:wght@300;400&family=Open+Sans:wght@300;400&display=swap">
<style>
  :root {
    --page-bg: #ffffff;
    --dark-start: #404042;
    --dark-end: #5b5b5d;
    --navy: #1c3768;
    --navy-rule: #3a5a85;
    --soft-grey: #b4b4b6;
    --card-border: #cfcfd1;
    --white: #ffffff;
  }
  * { margin: 0; padding: 0; box-sizing: border-box; }
  html, body {
    width: 1200px; height: 927px; overflow: hidden;
    background: var(--page-bg);
  }
  .sheet { position: relative; width: 1200px; height: 927px; }

  .card {
    position: absolute;
    width: 382px; height: 218px;
    overflow: hidden;
  }
  .card--dark { background: linear-gradient(90deg, var(--dark-start), var(--dark-end)); color: var(--white); }
  .card--light { background: var(--white); border: 2px solid var(--card-border); color: var(--navy); }

  .card--a { left: 182px; top: 191px; }
  .card--b { left: 663px; top: 191px; }
  .card--c { left: 176px; top: 535px; }
  .card--d { left: 657px; top: 535px; }

  .wordmark__descriptor {
    position: absolute; left: 45px; top: 18px;
    font-family: "Open Sans", sans-serif; font-weight: 300;
    font-size: 16px; letter-spacing: 3px; line-height: 1;
  }
  .card--light .wordmark__descriptor { color: var(--soft-grey); }

  .wordmark__name {
    position: absolute; left: 36px; top: 30px;
    font-family: "Oswald", sans-serif; font-weight: 300;
    font-size: 32px; letter-spacing: 6px; line-height: 1;
    transform: scaleY(1.12); transform-origin: left top;
  }

  .card__rule {
    position: absolute; left: 107px; right: 0; top: 67px;
    height: 2px; background: var(--white);
  }
  .card--light .card__rule { background: var(--navy-rule); top: 66px; }

  .card__services {
    position: absolute; left: 107px; top: 73px;
    font-family: "Open Sans", sans-serif; font-size: 10.5px; line-height: 1.2;
  }
  .card--light .card__services { color: var(--soft-grey); }

  .accreditation {
    position: absolute; width: 26px; height: 26px;
    border-radius: 50%;
    border: 2px solid currentColor;
    opacity: 0.85;
  }
  .card--dark .accreditation { color: #e6e6e6; }
  .accreditation--bottom { left: 270px; top: 176px; }
  .accreditation--top { left: 276px; top: 31px; }
</style>
</head>
<body>
<main class="sheet">

  <section class="card card--dark card--a">
    <p class="wordmark__descriptor">Builders</p>
    <p class="wordmark__name">Holloway</p>
    <div class="card__rule"></div>
    <p class="card__services">Building / Construction, Concrete, Steelwork.</p>
    <div class="accreditation accreditation--bottom" role="img" aria-label="Registered building practitioner badge"></div>
  </section>

  <section class="card card--light card--b">
    <p class="wordmark__descriptor">Builders</p>
    <p class="wordmark__name">Holloway</p>
    <div class="card__rule"></div>
    <p class="card__services">Building / Construction, Concrete, Steelwork.</p>
    <div class="accreditation accreditation--bottom" role="img" aria-label="Registered building practitioner badge"></div>
  </section>

  <section class="card card--dark card--c">
    <p class="wordmark__descriptor">Builders</p>
    <p class="wordmark__name">Holloway</p>
    <div class="accreditation accreditation--top" role="img" aria-label="Registered building practitioner badge"></div>
    <div class="card__rule"></div>
    <p class="card__services">Building / Construction, Concrete, Steelwork.</p>
  </section>

  <section class="card card--light card--d">
    <p class="wordmark__descriptor">Builders</p>
    <p class="wordmark__name">Holloway</p>
    <div class="accreditation accreditation--top" role="img" aria-label="Registered building practitioner badge"></div>
    <div class="card__rule"></div>
    <p class="card__services">Building / Construction, Concrete, Steelwork.</p>
  </section>

</main>
</body>
</html>
```